Varrow Business Card Design - Professional Flexible and forward thinking. Clean and Easy to follow

Management Consulting Company. I focus on business development and concept and operational review. I need a progressive, simple and professional layout design for the business cards, letterhead and envelops
Professional Flexible and forward thinking. Clean and Easy to follow
Mature Business persons and professionals and Corporations

Target Market(s)

Mature Business persons and professionals and Corporations - Government org.

Industry/Entity Type

Consulting

Contact Information for Business Card

Requirements
Must have
• Marcus Varrow
• President
• Phone - 347.682.1530
• email - Mvarrow@varrowpartners-example.com
• Skype - Marc.varrow
• 2187 Tollbrook Lane
• Suite 2C
• Kestrel Bay, C.T. 11492
• USA
Nice to have
• www.varrowpartners-example.com
Should not have
• N/A

```html
<!DOCTYPE html>
<html lang="en">
<head>
<meta charset="utf-8">
<title>Varrow Business Card Design</title>
<link href="https://fonts.googleapis.com/css2?family=Source+Sans+3:wght@400;600;700&display=swap" rel="stylesheet">
<style>
  :root {
    --brand-red: #e11d26;
    --ink: #2b2b2b;
    --card: #ffffff;
    --stage-top: #2a2a2a;
    --stage-bottom: #050505;
  }
  * { margin: 0; padding: 0; box-sizing: border-box; }
  html, body { width: 1200px; height: 900px; overflow: hidden; }
  body {
    position: relative;
    background: linear-gradient(180deg, var(--stage-top) 0%, #141414 55%, var(--stage-bottom) 100%);
    font-family: "Source Sans 3", Arial, sans-serif;
    color: var(--ink);
  }
  .card {
    position: absolute;
    top: 306px;
    width: 440px;
    height: 271px;
    background: var(--card);
    border-radius: 12px;
    box-shadow: 0 4px 14px rgba(0,0,0,0.45);
    overflow: hidden;
  }
  .card--front { left: 149px; }
  .card--back { left: 608px; }

  .wordmark {
    position: absolute;
    display: flex;
    align-items: center;
    color: var(--brand-red);
    font-weight: 600;
    letter-spacing: 1px;
    text-transform: uppercase;
    line-height: 1;
    white-space: nowrap;
  }
  .wordmark__dot {
    display: block;
    border-radius: 50%;
    background: var(--brand-red);
  }
  .card--front .wordmark { left: 28px; top: 117px; font-size: 34px; gap: 8px; }
  .card--front .wordmark__dot { width: 10px; height: 10px; }
  .card--back .wordmark { left: 0; right: 0; justify-content: center; top: 100px; font-size: 60px; gap: 14px; }
  .card--back .wordmark__dot { width: 18px; height: 18px; }

  .contact {
    position: absolute;
    left: 206px;
    top: 44px;
    font-size: 12.5px;
    line-height: 15.7px;
    white-space: nowrap;
  }
  .contact__name { color: var(--brand-red); font-weight: 700; font-size: 15px; line-height: 17px; }
  .contact__title { margin-bottom: 14px; }
  .contact__address { margin-bottom: 10px; }
  .contact__list { list-style: none; font-size: 12px; }
  .contact__item { display: flex; align-items: center; gap: 7px; }
  .contact__icon { width: 9px; height: 9px; flex: none; }
</style>
</head>
<body>
  <section class="card card--front">
    <div class="wordmark"><span class="wordmark__dot"></span>Varrow</div>
    <div class="contact">
      <p class="contact__name">Marcus Varrow</p>
      <p class="contact__title">President</p>
      <p class="contact__address">2187 Tollbrook Lane<br>Suite 2C<br>Kestrel Bay, C.T. 11492<br>USA</p>
      <ul class="contact__list">
        <li class="contact__item">
          <svg class="contact__icon" viewBox="0 0 10 10"><path d="M2 0.5 L3.8 2.6 L2.9 3.7 Q4 6 6.3 7.1 L7.4 6.2 L9.5 8 L8.2 9.5 Q1.8 8.6 0.5 1.8 Z" fill="var(--brand-red)"/></svg>
          347.682.1530
        </li>
        <li class="contact__item">
          <svg class="contact__icon" viewBox="0 0 10 10"><rect x="0.5" y="2" width="9" height="6.5" fill="var(--brand-red)"/><path d="M0.5 2 L5 5.5 L9.5 2" stroke="#fff" stroke-width="0.9" fill="none"/></svg>
          Mvarrow@varrowpartners-example.com
        </li>
        <li class="contact__item">
          <svg class="contact__icon" viewBox="0 0 10 10"><circle cx="5" cy="5" r="4.5" fill="var(--brand-red)"/><path d="M0.8 5 H9.2 M5 0.5 Q2.5 5 5 9.5 M5 0.5 Q7.5 5 5 9.5" stroke="#fff" stroke-width="0.7" fill="none"/></svg>
          www.varrowpartners-example.com
        </li>
        <li class="contact__item">
          <svg class="contact__icon" viewBox="0 0 10 10"><rect x="0.5" y="0.5" width="9" height="9" rx="1.5" fill="var(--brand-red)"/></svg>
          Marc.varrow
        </li>
      </ul>
    </div>
  </section>

  <section class="card card--back">
    <div class="wordmark"><span class="wordmark__dot"></span>Varrow</div>
  </section>
</body>
</html>
```